Brenmoss Building Company needs a flyer to catch attention

A flyer that can be displayed at several different stores detailing our skills, work produced, experience and contact details. Information can be extracted from our website www.brenmossbc.co.nz. The flyer should feel very green, with addition of pics of work completed as well as stock images of lush green plants, lawns, landscape or similar. Needs to be eye catching with just enough information to express our experience and commitment to high standards

Target Market(s)

Residential
Landscape Architects

Industry/Entity Type

Landscaping

Font styles to use
Serif

Colors
abd037

Requirements
Must have
• Our logo
Experience
Services offered including pictures
All information avail on our website www.brenmossbc.co.nz
Nice to have
• stock images of lush greenery like a garden after fresh rainfall
Should not have
• Nothing comes to mind

```html
<!DOCTYPE html>
<html lang="en">
<head>
<meta charset="utf-8">
<title>Brenmoss Building Company – Flyer</title>
<link rel="stylesheet" href="https://fonts.googleapis.com/css2?family=Libre+Baskerville:wght@400;700&family=Cormorant+Garamond:wght@400;500;600&display=swap">
<style>
  :root {
    --brand-green: #a5c462;
    --deep-green: #2f7d3a;
    --pale: #f3f7f1;
    --ink: #3a3a3a;
    --white: #ffffff;
  }
  * { margin: 0; padding: 0; box-sizing: border-box; }
  html, body { width: 854px; height: 1200px; overflow: hidden; background: var(--white); }
  .flyer { position: relative; width: 854px; height: 1200px; font-family: "Libre Baskerville", serif; color: var(--ink); }
  .abs { position: absolute; }

  /* intro panel */
  .intro { left: 46px; top: 47px; width: 759px; height: 212px; background: var(--brand-green); }
  .intro-text { left: 92px; top: 114px; color: var(--white); font-size: 19px; line-height: 31.5px; letter-spacing: 0.7px; }
  .brand-mark { left: 598px; top: 102px; width: 150px; text-align: center; }
  .brand-mark .dot { width: 90px; height: 90px; border-radius: 50%; background: var(--deep-green); margin: 0 auto 9px; }
  .brand-mark .name { color: var(--deep-green); font-size: 13px; font-weight: 700; line-height: 17px; }

  .photo-pool { left: 46px; top: 259px; width: 285px; height: 320px;
    background: linear-gradient(172deg, #3f4a36 0%, #5d6e4c 12%, #7fb1b3 24%, #9ec7c6 38%, #5f6462 48%, #d6d4cd 58%, #b9b7b0 72%, #e2e0da 86%, #a9a7a1 100%); }
  .photo-garden { left: 331px; top: 259px; width: 474px; height: 320px;
    background: linear-gradient(125deg, #6d6646 0%, #b3a47a 22%, #cbb98d 38%, #3f5a23 52%, #e6e8e0 62%, #56702f 74%, #8c7a52 88%, #cfc4a3 100%); }
  .web-band { left: 46px; top: 529px; width: 759px; height: 28px; background: var(--white); text-align: center; font-size: 12.5px; font-weight: 700; letter-spacing: 3px; line-height: 28px; color: #1c1c1c; }

  /* services panel */
  .services { left: 45px; top: 622px; width: 760px; height: 460px; background: linear-gradient(160deg, #ffffff 0%, var(--pale) 60%, #e8efe5 100%); border: 1px solid #e5ebe2; }
  .services-accent { left: 46px; top: 624px; width: 32px; height: 176px; background: var(--brand-green); }
  .leaf-glow { left: 160px; top: 680px; width: 200px; height: 230px; border-radius: 48% 52% 45% 55%;
    background: radial-gradient(ellipse at 50% 45%, rgba(70,160,70,0.7) 0%, rgba(120,190,100,0.45) 45%, rgba(200,230,190,0.15) 70%, rgba(255,255,255,0) 80%); }
  .services-title { left: 335px; top: 664px; width: 200px; text-align: center; font-family: "Cormorant Garamond", serif; font-size: 30px; letter-spacing: 4px; font-weight: 500; color: #2f2f2f; }
  .icon-row { left: 560px; top: 658px; display: flex; gap: 19px; }
  .icon-row svg { width: 38px; height: 38px; }
  .services-lead { left: 95px; top: 712px; width: 674px; text-align: center; font-family: "Cormorant Garamond", serif; font-size: 13.5px; line-height: 16px; letter-spacing: 1.2px; color: #333; }
  .service-list { top: 798px; width: 220px; text-align: center; list-style: none; font-family: "Cormorant Garamond", serif; font-size: 13px; font-weight: 500; line-height: 18px; letter-spacing: 2.2px; color: #333; }
  .col-1 { left: 85px; } .col-2 { left: 326px; } .col-3 { left: 566px; }

  .work-band { left: 786px; top: 907px; width: 19px; height: 175px; background: var(--brand-green); }
  .work-lawn { left: 87px; top: 907px; width: 231px; height: 175px;
    background: linear-gradient(170deg, #2c2a26 0%, #7a4a36 14%, #5d7c34 30%, #7fa448 42%, #c9c8c0 55%, #a8a79f 68%, #3f3d36 82%, #24231f 100%); }
  .work-fence { left: 322px; top: 907px; width: 231px; height: 175px;
    background: linear-gradient(100deg, #7a4c2b 0%, #b27b4a 25%, #9c6a3e 45%, #c89a6a 58%, #e7e9ec 72%, #9a9892 85%, #5e5c58 100%); }
  .work-patio { left: 556px; top: 907px; width: 230px; height: 175px;
    background: linear-gradient(180deg, #c9ced2 0%, #7b8c96 16%, #a4b0b6 26%, #6a6e6a 40%, #a6a49e 58%, #7d7b75 76%, #2c2c2a 100%); }

  .footer { left: 45px; top: 1082px; width: 760px; height: 74px; background: var(--brand-green); }
  .footer-brand { left: 150px; top: 1094px; display: flex; align-items: center; gap: 8px; }
  .footer-brand .dot { width: 48px; height: 48px; border-radius: 50%; background: #8fb25a; border: 2px solid #6f9a44; }
  .footer-brand .name { color: var(--white); font-size: 10.5px; font-weight: 700; line-height: 13px; }
  .contact { top: 1109px; display: flex; align-items: center; gap: 6px; font-size: 10.5px; font-weight: 700; letter-spacing: 1.2px; color: #1c1c1c; }
  .contact-phone { left: 390px; } .contact-mail { left: 510px; }
</style>
</head>
<body>
<main class="flyer">
  <section class="abs intro"></section>
  <p class="abs intro-text">More than 25 years experience<br>in the landscaping industry,<br>we offer services to large or small residential<br>and commercial projects.</p>
  <div class="abs brand-mark">
    <div class="dot"></div>
    <div class="name">Brenmoss Building<br>Company</div>
  </div>

  <div class="abs photo-pool" role="img" aria-label="Plunge pool with light timber decking and steps"></div>
  <div class="abs photo-garden" role="img" aria-label="Garden bed with palms and white flowering shrubs on gravel"></div>
  <div class="abs web-band">www.brenmossbc.co.nz</div>

  <section class="abs services"></section>
  <div class="abs services-accent"></div>
  <div class="abs leaf-glow" role="img" aria-label="Soft blurred green leaves"></div>
  <h2 class="abs services-title">SERVICES</h2>
  <div class="abs icon-row" aria-hidden="true">
    <svg viewBox="0 0 38 38"><circle cx="19" cy="19" r="17.5" fill="#fff" stroke="#9bbf5c" stroke-width="1.5"/><path d="M11 24 q6 -2 10 0 l5 -4" fill="none" stroke="#333" stroke-width="1.3"/><path d="M19 19 q0 -8 6 -9 q0 7 -6 9z" fill="none" stroke="#333" stroke-width="1.3"/></svg>
    <svg viewBox="0 0 38 38"><circle cx="19" cy="19" r="17.5" fill="#fff" stroke="#9bbf5c" stroke-width="1.5"/><path d="M10 23 h18 M19 23 v-7 M13 23 v-4 M25 23 v-4" stroke="#333" stroke-width="1.3"/><circle cx="19" cy="14" r="2" fill="none" stroke="#333" stroke-width="1.2"/></svg>
    <svg viewBox="0 0 38 38"><circle cx="19" cy="19" r="17.5" fill="#fff" stroke="#9bbf5c" stroke-width="1.5"/><path d="M11 27 v-12 l2 -2 l2 2 v12 M17 27 v-12 l2 -2 l2 2 v12 M23 27 v-12 l2 -2 l2 2 v12 M10 18 h18 M10 23 h18" fill="none" stroke="#333" stroke-width="1.2"/></svg>
    <svg viewBox="0 0 38 38"><circle cx="19" cy="19" r="17.5" fill="#fff" stroke="#9bbf5c" stroke-width="1.5"/><circle cx="15" cy="17" r="5" fill="none" stroke="#333" stroke-width="1.2"/><circle cx="23" cy="17" r="5" fill="none" stroke="#333" stroke-width="1.2"/><path d="M15 22 v5 M23 22 v5 M10 27 h18" stroke="#333" stroke-width="1.2"/></svg>
  </div>
  <p class="abs services-lead">As a full construction landscaping company, we formally offer the following services.<br>However, we regularly work with clients who want something a little out of the box.</p>
  <ul class="abs service-list col-1"><li>RETAINING WALLS</li><li>GARDENS &amp; LAWNS</li><li>IRRIGATION</li><li>PROJECT MANAGEMENT</li><li>CONSULTATION</li></ul>
  <ul class="abs service-list col-2"><li>FENCING</li><li>BOARDWALKS</li><li>TIMBER</li><li>PLANTER BOXES</li><li>PERGOLAS</li></ul>
  <ul class="abs service-list col-3"><li>PATIOS</li><li>PAVING</li><li>CONCRETE</li><li>WATER FEATURES</li><li>DECKING</li></ul>

  <div class="abs work-band"></div>
  <div class="abs work-lawn" role="img" aria-label="New lawn and concrete path beside a brick wall"></div>
  <div class="abs work-fence" role="img" aria-label="Horizontal timber slat fence"></div>
  <div class="abs work-patio" role="img" aria-label="Paved patio overlooking a lake"></div>

  <footer class="abs footer"></footer>
  <div class="abs footer-brand">
    <div class="dot"></div>
    <div class="name">Brenmoss Building<br>Company</div>
  </div>
  <div class="abs contact contact-phone">
    <svg width="12" height="20" viewBox="0 0 12 20" aria-hidden="true"><rect x="1" y="1" width="10" height="18" rx="1.5" fill="none" stroke="#fff" stroke-width="1.5"/><line x1="4" y1="16" x2="8" y2="16" stroke="#fff" stroke-width="1.2"/></svg>
    <span>021 555 014</span>
  </div>
  <div class="abs contact contact-mail">
    <svg width="18" height="13" viewBox="0 0 18 13" aria-hidden="true"><rect x="1" y="1" width="16" height="11" fill="none" stroke="#fff" stroke-width="1.3"/><path d="M1 1 l8 6 l8 -6 M1 12 l6 -5 M17 12 l-6 -5" fill="none" stroke="#fff" stroke-width="1.2"/></svg>
    <span>hello@brenmossbc.co.nz</span>
  </div>
</main>
</body>
</html>
```